Alloy wheel repair business needs a website

Install logo previously purchased from pixelbazaar, toolbar with dropdowns. services, gallery, clients , contact ect
Maybe mission statment

Target Market(s)

vehicle owners, auto dealers,insurance companies,

Industry/Entity Type

Alloy Wheel Repair

Coding

Coded - Design and coding required

Number of Pages Required

4 page

Font styles to use
Sans Serif

Colors
0054AA
0677BA
7BADD7
CADEEF
E8F1F8

```html
<!DOCTYPE html>
<html lang="en">
<head>
<meta charset="utf-8">
<title>Rimhaven Works — Alloy Wheel Restoration</title>
<link href="https://fonts.googleapis.com/css2?family=Barlow:wght@400;500;600;700&display=swap" rel="stylesheet">
<style>
:root{
  --ink:#1e1e1d;
  --blue:#468cc9;
  --mist:#f1f2f3;
  --board:#e1e1e1;
  --white:#ffffff;
  --grey-text:#6b6b6b;
  --dark:#0b0b0c;
}
*{box-sizing:border-box;margin:0;padding:0}
html,body{width:1200px;height:2815px;overflow:hidden}
body{background:var(--board);font-family:'Barlow',sans-serif;color:var(--ink);position:relative}
.abs{position:absolute}

/* presentation header */
.brand-mark{left:204px;top:128px;font-size:30px;font-weight:700;color:var(--blue);letter-spacing:1px}
.spec-title{font-size:25px;font-weight:500;color:var(--ink)}
.spec-fonts{left:597px;top:100px}
.spec-font-name{left:597px;top:148px;font-size:16px;color:#555}
.spec-colors{left:889px;top:100px}
.swatch{top:138px;width:42px;height:42px;border-radius:50%}
.swatch-label{top:188px;font-size:10px;color:#555;width:60px;text-align:center}

/* site */
.site{left:222px;top:271px;width:791px;height:2439px;background:var(--white)}
.nav{position:absolute;left:0;top:0;width:791px;height:39px}
.nav-logo{position:absolute;left:108px;top:9px;font-size:17px;font-weight:700;color:var(--blue)}
.nav-links{position:absolute;left:312px;top:14px;display:flex;gap:14px;font-size:8px;color:var(--ink)}
.nav-links .sep{color:#aaa}
.nav-search{position:absolute;left:674px;top:12px}

.hero{position:absolute;left:4px;top:39px;width:783px;height:420px;
  background:radial-gradient(ellipse at 78% 55%,#5b5e63 0%,#2d2f33 35%,#141518 70%),#141518}
.hero-wheel{position:absolute;right:30px;top:60px;width:250px;height:340px;border-radius:50%;
  background:radial-gradient(circle,#3a3d42 0%,#1b1c1f 60%,#0c0c0e 100%)}
.hero-tag{position:absolute;left:103px;top:210px;font-size:7px;letter-spacing:3px;color:var(--blue);font-weight:600}
.hero-title{position:absolute;left:102px;top:222px;font-size:40px;line-height:42px;font-weight:700;color:var(--white)}
.btn-outline{position:absolute;left:103px;top:330px;width:94px;height:33px;border:1px solid var(--blue);
  color:var(--white);font-size:8px;font-weight:600;display:flex;align-items:center;justify-content:center}
.btn-link{position:absolute;left:211px;top:344px;font-size:8px;color:var(--blue);font-weight:500}

.services{position:absolute;left:4px;top:466px;width:783px;height:148px;display:flex;gap:6px}
.svc{flex:1;background:var(--mist);position:relative}
.svc-img{position:absolute;left:12px;top:18px;width:100px;height:112px;border-radius:6px}
.svc h3{position:absolute;left:134px;top:26px;font-size:14px;line-height:16px;font-weight:600;width:110px}
.svc p{position:absolute;left:134px;top:66px;font-size:7px;line-height:12px;color:var(--grey-text);width:110px}
.svc a{position:absolute;left:134px;top:112px;font-size:8px;color:var(--blue);text-decoration:none}

.video{position:absolute;left:4px;top:621px;width:783px;height:183px;
  background:radial-gradient(ellipse at 75% 60%,#1f3f86 0%,#1a1b20 22%,#0e0e10 60%),#0e0e10}
.play{position:absolute;left:358px;top:58px;width:66px;height:66px;border-radius:50%;border:2px solid rgba(255,255,255,.6);
  background:rgba(255,255,255,.15)}

.what{position:absolute;left:0;top:804px;width:791px;height:316px}
.what-fade{position:absolute;right:0;top:0;width:160px;height:316px;
  background:linear-gradient(90deg,rgba(255,255,255,1),rgba(220,222,226,.6))}
.what h2{position:absolute;left:0;width:791px;top:56px;text-align:center;font-size:24px;font-weight:600}
.what .lead{position:absolute;left:243px;width:305px;top:97px;text-align:center;font-size:7.5px;line-height:13px;color:var(--grey-text)}
.what .lead b{color:var(--ink);font-weight:600}
.feat{position:absolute;top:168px;width:120px;text-align:center}
.feat svg{display:block;margin:0 auto 14px}
.feat h4{font-size:9px;font-weight:600;margin-bottom:5px}
.feat p{font-size:7px;line-height:11px;color:var(--grey-text)}

.gallery{position:absolute;left:4px;top:1120px;width:783px;height:401px;
  background:linear-gradient(135deg,#1a1a1c 0%,#050505 60%,#111 100%)}
.gallery h2{position:absolute;left:102px;top:56px;font-size:24px;line-height:27px;font-weight:600;color:var(--white)}
.arrow{position:absolute;top:130px;width:33px;height:33px;border-radius:50%;display:flex;align-items:center;justify-content:center}
.arrow.prev{left:102px;border:1px solid #888}
.arrow.next{left:140px;background:var(--blue)}
.view-all{position:absolute;left:102px;top:186px;font-size:8px;font-weight:600;color:var(--white)}
.shot{position:absolute;background:linear-gradient(135deg,#c8cacd,#6f7276 55%,#2b2c2f)}

.mission{position:absolute;left:4px;top:1521px;width:783px;height:239px;background:var(--mist)}
.mission h2{position:absolute;left:106px;top:56px;font-size:24px;line-height:27px;font-weight:500}
.mission .copy{position:absolute;left:395px;top:58px;width:275px;font-size:7.5px;line-height:13.5px;color:var(--grey-text)}
.points{position:absolute;left:395px;top:128px;display:flex;gap:18px}
.point{display:flex;gap:5px;font-size:8px;line-height:11px;color:var(--ink)}
.mission .tail{position:absolute;left:395px;top:163px;width:275px;font-size:7.5px;line-height:13px;color:var(--grey-text)}
.mission-img{position:absolute;left:-4px;top:142px;width:245px;height:115px;border-radius:50% 40% 10px 10px;
  background:linear-gradient(180deg,#d9dadc,#6d6f73 70%,#1d1d1f)}

.reviews{position:absolute;left:0;top:1760px;width:791px;height:351px}
.reviews h2{position:absolute;left:0;width:791px;top:47px;text-align:center;font-size:21px;font-weight:600}
.review{position:absolute;top:102px;width:182px;height:155px;background:var(--mist)}
.rev-head{position:absolute;left:0;top:0;width:182px;height:36px;border-bottom:1px solid #dcdcdc}
.avatar{position:absolute;left:14px;top:10px;width:17px;height:17px;border-radius:50%;background:#9aa0a8}
.rev-name{position:absolute;left:40px;top:11px;font-size:7px;font-weight:600}
.rev-time{position:absolute;left:40px;top:21px;font-size:6px;color:#888}
.rev-src{position:absolute;right:12px;top:14px;width:8px;height:8px;border:1px solid var(--blue);border-radius:50%}
.stars{position:absolute;left:12px;top:47px;font-size:8px;color:#f2b01e;letter-spacing:1px}
.rev-text{position:absolute;left:12px;top:61px;width:160px;font-size:7px;line-height:12.5px;color:var(--grey-text)}
.dots{position:absolute;left:373px;top:290px;display:flex;gap:4px}
.dots span{width:6px;height:6px;border-radius:50%;border:1px solid var(--blue)}
.dots span.on{background:var(--blue)}

.footer{position:absolute;left:4px;top:2111px;width:783px;height:323px;background:var(--dark);color:var(--white)}
.f-logo{position:absolute;left:102px;top:56px;font-size:17px;font-weight:700;color:var(--white)}
.socials{position:absolute;left:102px;top:92px;display:flex;gap:5px}
.socials span{width:16px;height:16px;border-radius:50%;background:var(--blue)}
.f-col{position:absolute}
.f-col h5{font-size:9px;font-weight:600;margin-bottom:12px}
.f-col p{font-size:6.5px;line-height:14px;color:#9a9a9a}
.sub-input{position:absolute;left:474px;top:85px;width:133px;height:24px;border-bottom:1px solid #555;font-size:6.5px;color:#888;padding-top:9px}
.sub-btn{position:absolute;left:608px;top:84px;width:74px;height:25px;background:var(--blue);font-size:7px;font-weight:600;display:flex;align-items:center;justify-content:center}
.f-bottom{position:absolute;left:0;top:291px;width:783px;height:1px;background:#2a2a2a}
.copyright{position:absolute;left:102px;top:303px;font-size:6px;color:var(--blue)}
.legal{position:absolute;left:474px;top:303px;display:flex;gap:32px;font-size:5.5px;color:#aaa;letter-spacing:.3px}
</style>
</head>
<body>

<!-- presentation header -->
<div class="abs brand-mark">RIMHAVEN WORKS</div>
<div class="abs spec-title spec-fonts">Fonts:</div>
<div class="abs spec-font-name">Barlow</div>
<div class="abs spec-title spec-colors">Colors:</div>
<div class="abs swatch" style="left:890px;background:var(--ink)"></div>
<div class="abs swatch" style="left:941px;background:var(--blue)"></div>
<div class="abs swatch" style="left:992px;background:var(--mist)"></div>
<div class="abs swatch-label" style="left:881px">#1e1e1d</div>
<div class="abs swatch-label" style="left:932px">#468cc9</div>
<div class="abs swatch-label" style="left:983px">#f1f2f3</div>

<div class="abs site">
  <header class="nav">
    <div class="nav-logo">RIMHAVEN WORKS</div>
    <nav class="nav-links">
      <span>Home</span><span class="sep">/</span><span>Services</span><span class="sep">/</span><span>Gallery</span><span class="sep">/</span><span>Clients</span><span class="sep">/</span><span>Contact</span>
    </nav>
    <svg class="nav-search" width="14" height="14" viewBox="0 0 14 14"><circle cx="6" cy="6" r="4.5" fill="none" stroke="#468cc9" stroke-width="1.2"/><line x1="9.3" y1="9.3" x2="12.5" y2="12.5" stroke="#468cc9" stroke-width="1.2"/></svg>
  </header>

  <section class="hero" role="img" aria-label="Dark sports car side view with black alloy wheel">
    <div class="hero-wheel"></div>
    <div class="hero-tag">YOUR PATH TO ALLOY REVIVAL!</div>
    <h1 class="hero-title">The Excellence in<br>Alloy Restoration</h1>
    <div class="btn-outline">How It Works &nbsp;›</div>
    <div class="btn-link">Schedule an Appointment &nbsp;›</div>
  </section>

  <section class="services">
    <div class="svc">
      <div class="svc-img" role="img" aria-label="Alloy wheel and tyre with blue repair pad" style="background:radial-gradient(circle,#cfd1d4,#6b6d70 60%,#2a2b2e)"></div>
      <h3>Wheel Repair Services</h3>
      <p>Restore &amp; rejuvenate any damaged wheels with great precision and care</p>
      <a>Request a Quote &nbsp;›</a>
    </div>
    <div class="svc">
      <div class="svc-img" role="img" aria-label="Wheel with wrenches and tools" style="background:radial-gradient(circle,#d6d8db,#86898d 60%,#3a3c40)"></div>
      <h3>Wheel Replace Services</h3>
      <p>Get back on the road swiftly and securely with our efficient wheel replacement service</p>
      <a>Request a Quote &nbsp;›</a>
    </div>
    <div class="svc">
      <div class="svc-img" role="img" aria-label="Paint spray gun" style="background:linear-gradient(160deg,#d9dbde,#9a9da1 60%,#2f6fb0)"></div>
      <h3>Custom Wheel Coloring</h3>
      <p>Express your unique and personalized style with our expert wheel coloring service.</p>
      <a>Request a Quote &nbsp;›</a>
    </div>
  </section>

  <section class="video" role="img" aria-label="Close-up of black alloy wheel and blue brake caliper">
    <div class="play"><svg width="66" height="66" viewBox="0 0 66 66"><polygon points="28,24 28,42 42,33" fill="#fff"/></svg></div>
  </section>

  <section class="what">
    <div class="what-fade" role="img" aria-label="Faded silver car"></div>
    <h2>What We Do</h2>
    <p class="lead">At Rimhaven Works, whether it is restoring, customizing, or replacing wheels, our commitment to excellence and <b>exceptional customer service guarantees</b> a seamless and satisfying experience for all your wheel needs</p>
    <div class="feat" style="left:103px">
      <svg width="36" height="36" viewBox="0 0 36 36"><circle cx="18" cy="18" r="15" fill="none" stroke="#1e1e1d" stroke-width="1.4"/><circle cx="18" cy="18" r="9" fill="none" stroke="#468cc9" stroke-width="2"/><circle cx="18" cy="18" r="3" fill="#1e1e1d"/></svg>
      <h4>Wheel Refinishing</h4><p>Vestibulum tortor risus, rutrum at congue sed ultricies finibus.</p>
    </div>
    <div class="feat" style="left:258px">
      <svg width="36" height="36" viewBox="0 0 36 36"><rect x="4" y="4" width="10" height="26" fill="none" stroke="#1e1e1d" stroke-width="1.4"/><circle cx="23" cy="15" r="9" fill="none" stroke="#468cc9" stroke-width="2"/><line x1="2" y1="32" x2="34" y2="32" stroke="#1e1e1d" stroke-width="1.4"/></svg>
      <h4>Wheel Straightening</h4><p>Vestibulum tortor risus, rutrum at congue sed ultricies finibus.</p>
    </div>
    <div class="feat" style="left:413px">
      <svg width="36" height="36" viewBox="0 0 36 36"><circle cx="16" cy="16" r="11" fill="none" stroke="#1e1e1d" stroke-width="1.4" stroke-dasharray="4 2"/><circle cx="16" cy="16" r="5" fill="none" stroke="#468cc9" stroke-width="2"/><line x1="23" y1="23" x2="33" y2="33" stroke="#1e1e1d" stroke-width="2"/></svg>
      <h4>Wheel Repair</h4><p>Vestibulum tortor risus, rutrum at congue sed ultricies finibus.</p>
    </div>
    <div class="feat" style="left:568px">
      <svg width="40" height="40" viewBox="0 0 40 40"><circle cx="15" cy="25" r="11" fill="none" stroke="#1e1e1d" stroke-width="1.4"/><circle cx="15" cy="25" r="6" fill="none" stroke="#468cc9" stroke-width="2"/><rect x="27" y="3" width="9" height="7" fill="none" stroke="#1e1e1d" stroke-width="1.4"/><line x1="31" y1="10" x2="27" y2="16" stroke="#1e1e1d" stroke-width="1.4"/></svg>
      <h4>Wheel Coloring</h4><p>Vestibulum tortor risus, rutrum at congue sed ultricies finibus.</p>
    </div>
  </section>

  <section class="gallery">
    <h2>Shots from<br>Our Gallery</h2>
    <div class="arrow prev"><svg width="12" height="10" viewBox="0 0 12 10"><path d="M5 1 1 5l4 4M1 5h10" fill="none" stroke="#fff" stroke-width="1.2"/></svg></div>
    <div class="arrow next"><svg width="12" height="10" viewBox="0 0 12 10"><path d="M7 1l4 4-4 4M11 5H1" fill="none" stroke="#fff" stroke-width="1.2"/></svg></div>
    <div class="view-all">View All Gallery &nbsp;<span style="color:var(--blue)">›</span></div>
    <div class="shot" style="left:301px;top:59px;width:182px;height:140px" role="img" aria-label="Damaged silver alloy wheel before repair"></div>
    <div class="shot" style="left:301px;top:200px;width:182px;height:141px" role="img" aria-label="Silver alloy wheel after repair"></div>
    <div class="shot" style="left:499px;top:59px;width:181px;height:140px" role="img" aria-label="Scuffed alloy wheel rim close-up"></div>
    <div class="shot" style="left:499px;top:200px;width:181px;height:141px" role="img" aria-label="Restored alloy wheel rim close-up"></div>
    <div class="shot" style="left:696px;top:59px;width:87px;height:140px" role="img" aria-label="Alloy wheel spokes"></div>
    <div class="shot" style="left:696px;top:200px;width:87px;height:141px" role="img" aria-label="Alloy wheel spokes restored"></div>
  </section>

  <section class="mission">
    <h2>Mission<br>Statement</h2>
    <p class="copy">At Rimhaven Works, our mission is to deliver an unparalleled quality and craftsmanship in alloy wheel repair and customization services, enhancing the aesthetic and functional performance of vehicles while ensuring the customer satisfaction through our dedication to excellence.</p>
    <div class="points">
      <div class="point"><svg width="10" height="10" viewBox="0 0 10 10"><circle cx="5" cy="5" r="4.3" fill="none" stroke="#468cc9"/><path d="M3 5l1.5 1.5L7 3.8" fill="none" stroke="#468cc9"/></svg><span>Precision<br>Restoration</span></div>
      <div class="point"><svg width="10" height="10" viewBox="0 0 10 10"><circle cx="5" cy="5" r="4.3" fill="none" stroke="#468cc9"/><path d="M3 5l1.5 1.5L7 3.8" fill="none" stroke="#468cc9"/></svg><span>Customization<br>Expertise</span></div>
      <div class="point"><svg width="10" height="10" viewBox="0 0 10 10"><circle cx="5" cy="5" r="4.3" fill="none" stroke="#468cc9"/><path d="M3 5l1.5 1.5L7 3.8" fill="none" stroke="#468cc9"/></svg><span>Exceptional<br>Customer Service</span></div>
    </div>
    <p class="tail">From minor cosmetic damage to complete restoration, Rimhaven Works Specialists offers professional and affordable alloy rim repair.</p>
    <div class="mission-img" role="img" aria-label="Silver car with a stack of tyres"></div>
  </section>

  <section class="reviews">
    <h2>Client Reviews</h2>
    <div class="review" style="left:106px">
      <div class="rev-head"><div class="avatar"></div><div class="rev-name">Dana Whitlow</div><div class="rev-time">14 Hours Ago</div><div class="rev-src"></div></div>
      <div class="stars">★★★★★</div>
      <p class="rev-text">Rimhaven Works exceeded my expectations with their wheel repair service. My scratched and dented wheels looked brand new after their meticulous work. I couldn't be happier with the results!</p>
    </div>
    <div class="review" style="left:304px">
      <div class="rev-head"><div class="avatar"></div><div class="rev-name">Dana Whitlow</div><div class="rev-time">14 Hours Ago</div><div class="rev-src"></div></div>
      <div class="stars">★★★★★</div>
      <p class="rev-text">I wanted to give my car a fresh look, and Rimhaven Works did an amazing job with custom wheel coloring. They helped me choose the perfect finish, and now my car stands out wherever I go. Highly recommended and a place to go!</p>
    </div>
    <div class="review" style="left:502px">
      <div class="rev-head"><div class="avatar"></div><div class="rev-name">Dana Whitlow</div><div class="rev-time">14 Hours Ago</div><div class="rev-src"></div></div>
      <div class="stars">★★★★★</div>
      <p class="rev-text">When I needed a wheel replacement in a hurry, Rimhaven Works came to the rescue. Their quick and professional service got me back on the road safely. Many thanks for your expertise and efficiency</p>
    </div>
    <div class="dots"><span></span><span></span><span class="on"></span><span></span><span></span></div>
  </section>

  <footer class="footer">
    <div class="f-logo">RIMHAVEN WORKS</div>
    <div class="socials"><span></span><span></span><span></span></div>
    <div class="f-col" style="left:349px;top:60px"><h5>Sitemap</h5><p>About<br>Our Services<br>Project Gallery<br>Clients<br>Contact Us</p></div>
    <div class="f-col" style="left:474px;top:60px"><h5>Become an Rimhaven Works Insider</h5></div>
    <div class="sub-input">Enter Your Email Address</div>
    <div class="sub-btn">Subscribe Now</div>
    <div class="f-col" style="left:349px;top:180px"><h5>Working Hours</h5><p>Mon - Fri<br>09:00 AM - 05:00 PM<br>Sun - CLOSED</p></div>
    <div class="f-col" style="left:474px;top:180px"><h5>Contact Info</h5><p>hello@rimhavenworks.com<br>555 014 2288</p></div>
    <div class="f-col" style="left:614px;top:180px"><h5>Address</h5><p>42 Foundry Lane,<br>Westbrook PA 10000</p></div>
    <div class="f-bottom"></div>
    <div class="copyright">© 2023. All rights reserved.</div>
    <div class="legal"><span>PRIVACY POLICY</span><span>COOKIES POLICY</span><span>TERMS &amp; CONDITIONS</span></div>
  </footer>
</div>

</body>
</html>
```